I'm looking for an app for customers to order through

I'm looking for an app for my customers to order products through
Ideally each customer would have a customer number with password
Their profile would come up with a preloaded products they currently order
From there they can select the product they require and volume needed for delivery
I would also like an option for them to go to a full product range if they are looking for Ideas or a product they don't currently use
Once the order is completed a copy of the order is them e-mailed to my distribution facilities and a confirmation sent to the customer by e-mail and/or SMS
Current product list is approx 1000 items
Current customers is 80 with expectations to expand to 200
On average current products ordered by each customer is is between 4-8 items
Ordering units are done by both weight and pieces/units

Target Market(s)

Food service outlets,
Restaurant , Hotels, catering companies, clubs, take away shops, cafes
Retail outlets

Number of Pages Required

1 page

Font styles to use
Sans Serif

Colors
abd037

Requirements
Must have
• Customer log in with Password 4 - 6 digit
• Customer order history
Nice to have
• Area for promotions / specials on a weekly / monthly basis

```html
<!DOCTYPE html>
<html lang="en">
<head>
<meta charset="utf-8">
<title>Harvest Pantry – Ordering App Screens</title>
<link href="https://fonts.googleapis.com/css2?family=Nunito+Sans:wght@300;400;600&display=swap" rel="stylesheet">
<style>
:root{
  --page:#f4f4f4;
  --appbar:#255e2a;
  --brand:#7ea33b;
  --brand-text:#6a9a2a;
  --ink:#1d1d1d;
  --blue:#1f4fa0;
  --orange:#ef6c00;
  --orange-light:#ff9a1f;
  --amber:#f08a00;
  --red:#d32f2f;
  --brown:#7a3a12;
  --meat:#b5332b;
  --teal:#0b6a73;
  --brandtile:#8f1c1c;
  --steel:#c9d0d6;
  --scrim:rgba(0,0,0,.45);
}
*{margin:0;padding:0;box-sizing:border-box}
html,body{width:1200px;height:1051px;overflow:hidden;background:var(--page);font-family:"Nunito Sans",sans-serif}
.screen{position:absolute;top:28px;width:560px;height:996px;overflow:hidden;background:#fafafa;box-shadow:0 2px 6px rgba(0,0,0,.15)}
.screen--catalog{left:28px}
.screen--menu{left:612px}
.abs{position:absolute}
.appbar{left:0;top:0;width:560px;height:70px;background:var(--appbar);color:#fff;display:flex;align-items:center}
.appbar__title{position:absolute;left:81px;font-size:20px;letter-spacing:.5px;opacity:.9}
.tile{position:absolute;overflow:hidden;border-radius:2px}
.tile__photo{position:absolute;left:0;top:0;width:100%}
.tile__band{position:absolute;left:0;bottom:0;width:100%;color:#fff;padding:14px 12px}
.tile__name{font-size:20px;font-weight:300;white-space:nowrap}
.tile__price{font-size:15px;font-weight:300;opacity:.85}
.section-label{position:absolute;left:32px;font-size:16px;color:var(--ink)}
.section-more{position:absolute;left:484px;font-size:16px;color:#2e7d32;letter-spacing:1px}
.scrim{left:0;top:70px;width:560px;height:926px;background:var(--scrim)}
.popup{left:97px;top:266px;width:366px;height:463px;background:var(--orange);box-shadow:0 8px 24px rgba(0,0,0,.4)}
.popup__photo{left:0;top:0;width:366px;height:308px;background:radial-gradient(ellipse at 60% 75%,#6b5a2a 0%,#2a1e18 35%,#0c0c0c 70%)}
.popup__name{left:21px;top:322px;font-size:30px;font-weight:300;color:#fff;letter-spacing:1px}
.popup__unit{left:21px;top:362px;font-size:15px;font-weight:300;color:rgba(255,255,255,.85)}
.popup__total-label{left:21px;top:396px;font-size:16px;font-weight:300;color:rgba(255,255,255,.85)}
.popup__total{left:21px;top:416px;font-size:22px;font-weight:300;color:#fff}
.qty{left:268px;top:402px;width:77px;height:40px;background:var(--orange-light);color:#fff;font-size:17px;display:flex;align-items:center;padding-left:11px}
.qty svg{position:absolute;right:10px;top:17px}
.fab{position:absolute;border-radius:50%;background:var(--red);box-shadow:0 3px 8px rgba(0,0,0,.35);display:flex;align-items:center;justify-content:center}
.drawer{left:0;top:0;width:414px;height:996px;background:#fff;box-shadow:4px 0 12px rgba(0,0,0,.3)}
.drawer__header{left:0;top:0;width:414px;height:258px;background:var(--brand)}
.wordmark{left:54px;top:88px;display:flex;align-items:center;gap:14px}
.wordmark__dot{width:84px;height:84px;border-radius:50%;background:#efeee3}
.wordmark__name{font-size:38px;font-weight:600;color:#22331a;line-height:1.05}
.nav{left:0;width:414px}
.nav__item{position:absolute;left:0;width:414px;height:60px;display:flex;align-items:center}
.nav__item--active{background:#eeeeee}
.nav__icon{position:absolute;left:34px;width:32px;height:32px}
.nav__label{position:absolute;left:102px;font-size:22px;letter-spacing:.8px;color:var(--ink)}
.nav__item--active .nav__label{color:var(--brand-text)}
.divider{left:0;top:529px;width:414px;height:1px;background:#d6d6d6}
</style>
</head>
<body>

<!-- Catalog screen -->
<section class="screen screen--catalog">
  <header class="abs appbar">
    <svg class="abs" style="left:23px;top:24px" width="38" height="24" viewBox="0 0 38 24"><g stroke="#fff" stroke-width="2" opacity=".8"><line x1="0" y1="2" x2="36" y2="2"/><line x1="0" y1="9" x2="30" y2="9"/><line x1="0" y1="16" x2="24" y2="16"/><line x1="0" y1="23" x2="12" y2="23"/></g></svg>
    <span class="appbar__title">All Products</span>
    <svg class="abs" style="left:514px;top:22px" width="26" height="26" viewBox="0 0 26 26"><circle cx="10" cy="10" r="8" fill="none" stroke="#fff" stroke-width="2.4" opacity=".8"/><line x1="16" y1="16" x2="24" y2="24" stroke="#fff" stroke-width="3" opacity=".8"/></svg>
  </header>

  <div class="tile" style="left:32px;top:96px;width:181px;height:338px">
    <div class="tile__photo" role="img" aria-label="Blocks of butter in a bowl" style="height:262px;background:linear-gradient(160deg,#f1e8c4,#d9cf9a 50%,#1f2a3a)"></div>
    <div class="tile__band" style="height:76px;background:var(--blue)"><div class="tile__name">Butter</div><div class="tile__price">$20 / kg</div></div>
  </div>
  <div class="tile" style="left:218px;top:96px;width:181px;height:338px">
    <div class="tile__photo" role="img" aria-label="Bottles of oil" style="height:338px;background:linear-gradient(180deg,#0c0c0c,#2a1a18)"></div>
  </div>
  <div class="tile" style="left:410px;top:96px;width:160px;height:338px">
    <div class="tile__photo" role="img" aria-label="Bowls of ground spices" style="height:262px;background:linear-gradient(160deg,#5a4a4e,#c89838 55%,#e8e2dc)"></div>
    <div class="tile__band" style="height:76px;background:var(--amber)"><div class="tile__name">Spices</div><div class="tile__price">$15 / kg</div></div>
  </div>

  <div class="section-label" style="top:468px">Top Brands</div>
  <div class="section-more" style="top:470px">MORE</div>
  <div class="tile" style="left:32px;top:510px;width:181px;height:155px;background:var(--brandtile)"><div class="abs" style="left:30px;top:38px;width:80px;height:80px;border-radius:50%;background:#e8d9a8"></div></div>
  <div class="tile" style="left:218px;top:510px;width:181px;height:155px;background:#f2f2f2"></div>
  <div class="tile" style="left:410px;top:510px;width:160px;height:155px;background:var(--steel)"><div class="abs" style="left:60px;top:50px;width:70px;height:55px;background:#2a4f86"></div></div>

  <div class="section-label" style="top:698px">Recent Orders</div>
  <div class="section-more" style="top:700px">MORE</div>

  <div class="tile" style="left:32px;top:740px;width:181px;height:228px">
    <div class="tile__photo" role="img" aria-label="Loaf of cheese on a board" style="height:150px;background:linear-gradient(160deg,#8a6a40,#4a3220 60%,#241810)"></div>
    <div class="tile__band" style="height:78px;background:var(--brown)"><div class="tile__name">Cheese</div><div class="tile__price">$300</div></div>
  </div>
  <div class="tile" style="left:218px;top:740px;width:181px;height:228px">
    <div class="tile__photo" role="img" aria-label="Raw cut of meat with rosemary" style="height:150px;background:linear-gradient(160deg,#5a3a3a,#8a3a44 50%,#3a2a2a)"></div>
    <div class="tile__band" style="height:78px;background:var(--meat)"><div class="tile__name">Goat Meat</div><div class="tile__price">$800</div></div>
  </div>
  <div class="tile" style="left:410px;top:740px;width:160px;height:228px">
    <div class="tile__photo" role="img" aria-label="Fresh basil leaves" style="height:150px;background:linear-gradient(160deg,#5a9a3a,#2e6a22 60%,#cfe0c0)"></div>
    <div class="tile__band" style="height:78px;background:var(--teal)"><div class="tile__name">Natural Herbs</div><div class="tile__price">$100</div></div>
  </div>

  <div class="abs scrim"></div>

  <article class="abs popup">
    <div class="abs popup__photo" role="img" aria-label="Bottles of oil with limes, chilli and orange"></div>
    <div class="fab" style="left:388px;top:548px;width:58px;height:58px">
      <svg width="26" height="22" viewBox="0 0 26 22"><path d="M1 8h24l-4 13H5z M8 8l5-7 5 7" fill="#fff" stroke="#fff" stroke-width="1.5" stroke-linejoin="round"/><path d="M9 14l3 3 5-5" fill="none" stroke="var(--red)" stroke-width="2"/></svg>
    </div>
    <div class="abs popup__name">Meat Oil</div>
    <div class="abs popup__unit">$40 / bottle</div>
    <div class="abs popup__total-label">Total</div>
    <div class="abs popup__total">$800 approx</div>
    <div class="abs qty">20<svg width="10" height="6" viewBox="0 0 10 6"><path d="M0 0h10L5 6z" fill="#fff"/></svg></div>
  </article>
</section>

<!-- Navigation drawer screen -->
<section class="screen screen--menu">
  <div class="abs" role="img" aria-label="Dark product photograph" style="left:414px;top:0;width:146px;height:358px;background:linear-gradient(180deg,#0a0a0a,#3a3a3a 60%,#1a1a1a)"></div>
  <div class="abs" style="left:414px;top:358px;width:146px;height:272px;background:#f2f2f2"></div>
  <div class="abs" style="left:418px;top:540px;font-size:16px;color:#555">ers</div>
  <div class="abs" role="img" aria-label="Fresh basil leaves" style="left:414px;top:630px;width:146px;height:262px;background:linear-gradient(160deg,#5a9a3a,#2e6a22 60%,#cfe0c0)"></div>
  <div class="abs" style="left:414px;top:892px;width:146px;height:78px;background:var(--teal);color:#fff;padding:14px 8px">
    <div class="tile__name">Natural Herbs</div><div class="tile__price">$100</div>
  </div>
  <div class="abs" style="left:414px;top:0;width:146px;height:996px;background:var(--scrim)"></div>
  <div class="fab" style="left:472px;top:330px;width:56px;height:56px">
    <svg width="24" height="24" viewBox="0 0 24 24"><path d="M3 21l1-5L16 4l4 4L8 20z M14 6l4 4" fill="none" stroke="#fff" stroke-width="1.8" stroke-linejoin="round"/></svg>
  </div>

  <nav class="abs drawer">
    <div class="abs drawer__header">
      <div class="abs wordmark"><span class="wordmark__dot"></span><span class="wordmark__name">HARVEST<br>PANTRY</span></div>
    </div>

    <div class="abs nav" style="top:0">
      <div class="nav__item nav__item--active" style="top:276px">
        <svg class="nav__icon" viewBox="0 0 32 32"><path d="M16 4L2 16h4v12h7v-8h6v8h7V16h4z" fill="var(--brand-text)"/></svg>
        <span class="nav__label">Home</span>
      </div>
      <div class="nav__item" style="top:337px">
        <svg class="nav__icon" viewBox="0 0 32 32"><rect x="3" y="6" width="26" height="21" rx="4" fill="none" stroke="#111" stroke-width="2.6"/><line x1="3" y1="12" x2="29" y2="12" stroke="#111" stroke-width="2.6"/><rect x="19" y="17" width="10" height="5" fill="#111"/></svg>
        <span class="nav__label">All Products</span>
      </div>
      <div class="nav__item" style="top:396px">
        <svg class="nav__icon" viewBox="0 0 32 32"><path d="M2 12h28l-4 15H6z" fill="#111"/><path d="M9 12l7-8 7 8" fill="none" stroke="#111" stroke-width="2.4"/><path d="M11 19l4 4 6-6" fill="none" stroke="#fff" stroke-width="2.4"/></svg>
        <span class="nav__label">My Cart</span>
      </div>
      <div class="nav__item" style="top:452px">
        <svg class="nav__icon" viewBox="0 0 32 32"><path d="M2 6h18v16H2z M20 11h6l4 6v5H20z" fill="#111"/><circle cx="8" cy="24" r="3.4" fill="#111" stroke="#fff" stroke-width="1.5"/><circle cx="24" cy="24" r="3.4" fill="#111" stroke="#fff" stroke-width="1.5"/></svg>
        <span class="nav__label">Pending Orders</span>
      </div>
    </div>

    <div class="abs divider"></div>

    <div class="abs nav" style="top:0">
      <div class="nav__item" style="top:547px">
        <svg class="nav__icon" viewBox="0 0 32 32"><g fill="#111"><circle cx="16" cy="16" r="10"/><g stroke="#111" stroke-width="5"><line x1="16" y1="2" x2="16" y2="30"/><line x1="2" y1="16" x2="30" y2="16"/><line x1="6" y1="6" x2="26" y2="26"/><line x1="26" y1="6" x2="6" y2="26"/></g></g><circle cx="16" cy="16" r="4.5" fill="#fff"/></svg>
        <span class="nav__label">Settings</span>
      </div>
      <div class="nav__item" style="top:609px">
        <svg class="nav__icon" viewBox="0 0 32 32"><path d="M10 10a6 6 0 1 1 8 6c-2 1-2 3-2 5" fill="none" stroke="#111" stroke-width="2.4"/><circle cx="16" cy="28" r="1.8" fill="#111"/></svg>
        <span class="nav__label">F.A.Q</span>
      </div>
      <div class="nav__item" style="top:671px">
        <svg class="nav__icon" viewBox="0 0 32 32"><path d="M3 4h26v20H8l-5 5z" fill="#111"/><g stroke="#fff" stroke-width="2.2"><line x1="8" y1="10" x2="24" y2="10"/><line x1="8" y1="15" x2="24" y2="15"/><line x1="8" y1="20" x2="19" y2="20"/></g></svg>
        <span class="nav__label">Send Feedback</span>
      </div>
      <div class="nav__item" style="top:739px">
        <svg class="nav__icon" viewBox="0 0 32 32"><path d="M16 3l3.9 8.4 9.1 1-6.8 6.2 1.9 9L16 23l-8.1 4.6 1.9-9L3 12.4l9.1-1z" fill="none" stroke="#111" stroke-width="2.4" stroke-linejoin="round"/></svg>
        <span class="nav__label">Rate Us</span>
      </div>
    </div>
  </nav>
</section>

</body>
</html>
```